Law Offices business card

Hi there, I'll need business card for the Law Offices of Tobin Haskell. The information must convey his strategic approach and quick resolution to complex business litigation needs. Please emphasize Civil Litigation, Corporate Law, Business Governance and Real Estate Law. Tobin has over 25 years of experience in these fields.The card should be modern and edgy and the message should be clear. Please consult his current website for ideas.

Business

```html
<!DOCTYPE html>
<html lang="en">
<head>
<meta charset="utf-8">
<title>Law Offices of Tobin Haskell – Business Card</title>
<link href="https://fonts.googleapis.com/css2?family=Lato:wght@300;400;700&family=Lora:wght@400&display=swap" rel="stylesheet">
<style>
  :root {
    --page-bg: #e9e9e7;
    --card-bg: #f4f5f6;
    --band-dark: #cfd0d2;
    --band-light: #e2e3e5;
    --ink-strong: #3a3a3c;
    --ink-soft: #6b6c6f;
    --mark-grey: #8a8b8e;
  }
  html, body {
    margin: 0;
    width: 1200px;
    height: 1200px;
    overflow: hidden;
    background: var(--page-bg);
  }
  .stage {
    width: 1200px;
    height: 1200px;
    display: flex;
    flex-direction: column;
    align-items: center;
    justify-content: center;
    gap: 44px;
  }
  .business-card {
    width: 900px;
    height: 514px;
    display: block;
    box-shadow: 0 6px 24px rgba(0,0,0,0.12);
    font-family: "Lato", sans-serif;
  }
  .card-face { fill: var(--card-bg); }
  .band-outer { fill: var(--band-dark); }
  .band-inner { fill: var(--band-light); }
  .attorney-name { fill: var(--ink-strong); font-weight: 700; font-size: 46px; letter-spacing: 1px; }
  .attorney-title { fill: var(--ink-soft); font-weight: 300; font-size: 40px; }
  .firm-name { fill: var(--ink-strong); font-weight: 400; font-size: 44px; }
  .address-line { fill: var(--ink-soft); font-weight: 300; font-size: 29px; }
  .contact-line { fill: var(--ink-soft); font-weight: 300; font-size: 28px; letter-spacing: 0.5px; }
  .brand-square { fill: var(--mark-grey); }
  .brand-name { fill: var(--mark-grey); font-weight: 700; font-size: 44px; }
  .back-heading { fill: var(--ink-strong); font-family: "Lora", serif; font-size: 48px; letter-spacing: 2px; }
  .practice-area { fill: var(--ink-soft); font-family: "Lora", serif; font-size: 30px; letter-spacing: 1px; }
</style>
</head>
<body>
<main class="stage">
  <svg class="business-card card-front" viewBox="0 0 1050 600" xmlns="http://www.w3.org/2000/svg">
    <rect class="card-face" x="0" y="0" width="1050" height="600"/>
    <path class="band-outer" d="M0 0 H820 C640 40 300 120 0 380 Z"/>
    <path class="band-inner" d="M0 0 H560 C400 30 180 100 0 250 Z"/>

    <text class="attorney-name" x="990" y="100" text-anchor="end">TOBIN HASKELL</text>
    <text class="attorney-title" x="990" y="150" text-anchor="end">Attorney</text>
    <text class="firm-name" x="990" y="215" text-anchor="end">Law Offices of Tobin Haskell, P.A</text>
    <text class="address-line" x="990" y="272" text-anchor="end">118B Harbor Lane</text>
    <text class="address-line" x="990" y="312" text-anchor="end">Coral Bay, Florida 33912</text>

    <text class="contact-line" x="990" y="410" text-anchor="end">555-014-2736</text>
    <text class="contact-line" x="990" y="446" text-anchor="end">555-019-4821</text>
    <text class="contact-line" x="990" y="482" text-anchor="end">tobin@haskelllaw.com</text>
    <text class="contact-line" x="990" y="518" text-anchor="end">www.haskelllaw.com</text>

    <rect class="brand-square" x="60" y="486" width="40" height="40"/>
    <text class="brand-name" x="116" y="522">Haskell Law</text>
  </svg>

  <svg class="business-card card-back" viewBox="0 0 1050 600" xmlns="http://www.w3.org/2000/svg">
    <rect class="card-face" x="0" y="0" width="1050" height="600"/>
    <path class="band-outer" d="M1050 600 H620 C800 560 920 480 1050 300 Z"/>

    <text class="back-heading" x="80" y="140">Strategic Business Litigation</text>
    <text class="practice-area" x="80" y="230">Civil Litigation · Corporate Law</text>
    <text class="practice-area" x="80" y="280">Business Governance · Real Estate Law</text>
    <text class="back-heading" x="80" y="400">Over 25 Years of</text>
    <text class="back-heading" x="80" y="465">Trusted Legal Services</text>
  </svg>
</main>
</body>
</html>
```